Looking for a clean, modern, and professional business card design that reflects Valtrim Systems

The design should include the company logo, contact details, and align with our brand identity. Please use a sophisticated and minimalist style, incorporating [specific colors, if applicable]. Creativity is welcome, but the card must maintain a polished and professional appearance.

Details to Include:

Name: Gavin Trelowe
Title: VP Sales / Operations
Company: Valtrim Systems
Phone: 483.216.7705
Email: gavin@valtrimsystems-example.com
Website: www.valtrimsystems-example.com

```html
<!DOCTYPE html>
<html lang="en">
<head>
<meta charset="utf-8">
<title>Valtrim Systems — Business Card</title>
<link rel="stylesheet" href="https://fonts.googleapis.com/css2?family=Mulish:wght@400;600;800&display=swap">
<style>
  :root {
    --bg: #b9b9b9;
    --card-white: #ffffff;
    --card-black: #121212;
    --ink: #1a1a1a;
    --brand-blue: #3b78c0;
    --muted: #2b2b2b;
  }
  * { box-sizing: border-box; margin: 0; padding: 0; }
  html, body { width: 1200px; height: 781px; overflow: hidden; }
  body {
    background: var(--bg);
    font-family: "Mulish", Arial, sans-serif;
    display: flex;
    align-items: center;
    justify-content: center;
    gap: 40px;
  }
  .card {
    width: 520px;
    height: 297px;
    border-radius: 2px;
    box-shadow: 0 10px 24px rgba(0,0,0,0.25);
    position: relative;
    overflow: hidden;
  }
  .card--front { background: var(--card-white); color: var(--ink); }
  .card--back {
    background: var(--card-black);
    display: flex;
    align-items: center;
    justify-content: center;
  }
  .brand {
    display: flex;
    align-items: center;
    gap: 9px;
    font-weight: 800;
    letter-spacing: 0.02em;
    line-height: 1;
    white-space: nowrap;
  }
  .brand__mark { width: 13px; height: 13px; background: var(--brand-blue); flex: none; }
  .card--front .brand {
    position: absolute;
    left: 28px;
    top: 112px;
    width: 212px;
    font-size: 21px;
    color: var(--ink);
  }
  .card--back .brand { font-size: 40px; color: #ffffff; }
  .card--back .brand__mark { width: 20px; height: 20px; }
  .divider {
    position: absolute;
    left: 262px;
    top: 62px;
    width: 1.5px;
    height: 172px;
    background: var(--ink);
  }
  .contact {
    position: absolute;
    left: 284px;
    top: 70px;
    right: 16px;
  }
  .contact__name {
    font-size: 22px;
    font-weight: 800;
    color: var(--brand-blue);
  }
  .contact__title {
    font-size: 13px;
    font-weight: 400;
    color: var(--muted);
    margin-top: 2px;
    margin-bottom: 18px;
  }
  .contact__list { list-style: none; }
  .contact__item {
    display: flex;
    align-items: center;
    gap: 7px;
    font-size: 11.5px;
    color: var(--muted);
    margin-bottom: 9px;
    white-space: nowrap;
  }
  .contact__item--phone { font-size: 14px; letter-spacing: 0.12em; }
  .contact__icon { width: 10px; height: 10px; flex: none; fill: var(--brand-blue); }
</style>
</head>
<body>
  <section class="card card--front" aria-label="Business card front">
    <div class="brand"><span class="brand__mark"></span>Valtrim Systems</div>
    <div class="divider"></div>
    <div class="contact">
      <h1 class="contact__name">Gavin Trelowe</h1>
      <p class="contact__title">VP Sales / Operations</p>
      <ul class="contact__list">
        <li class="contact__item contact__item--phone">
          <svg class="contact__icon" viewBox="0 0 10 10" aria-hidden="true"><path d="M2 0.5 L3.6 0.5 L4.2 3 L3 3.8 Q4 6 6.2 7 L7 5.8 L9.5 6.4 L9.5 8 Q9.5 9.5 8 9.5 Q0.5 9 0.5 2 Q0.5 0.5 2 0.5Z"/></svg>
          483.216.7705
        </li>
        <li class="contact__item">
          <svg class="contact__icon" viewBox="0 0 10 10" aria-hidden="true"><path d="M0 2 H10 V8.5 H0 Z M0.8 2.6 L5 5.8 L9.2 2.6" stroke="#fff" stroke-width="0.8"/></svg>
          gavin@valtrimsystems-example.com
        </li>
        <li class="contact__item">
          <svg class="contact__icon" viewBox="0 0 10 10" aria-hidden="true"><circle cx="5" cy="5" r="4.6"/><path d="M0.4 5 H9.6 M5 0.4 V9.6 M5 0.4 Q2 5 5 9.6 M5 0.4 Q8 5 5 9.6" stroke="#fff" stroke-width="0.6" fill="none"/></svg>
          www.valtrimsystems-example.com
        </li>
      </ul>
    </div>
  </section>

  <section class="card card--back" aria-label="Business card back">
    <div class="brand"><span class="brand__mark"></span>Valtrim Systems</div>
  </section>
</body>
</html>
```